PostCard Design Project

I am making a mailing postcard
I am having the mailing printed using 4 color foil on certain parts.
I am looking for a design that maximizes the foil process where certain parts are done in foil to grab the customers attention (example: if there is a car on the postcard the headlights would be done in foil) .
I am targeting some industries, (auto, real estate, medical, beauty) I would like the post card to have examples of postcard ideas for 2 or 3 of these industries.
specs:
the postcard should be atleast 6.5x9 up to 8.5x11, I don't want to restrict the space for the creative as I don't want everything to look like a huge mess. both sides will be used.
the piece is a direct mail piece so it has to meet requirements of https://www.kelvanepost.example/business/pdf/quick-reference-guide.pdf
text will be
"business with no limits, meet mailing with no addresses, gain new customers through "Open Lane Parcel Drop" reach new customers at their home without needing their address. "
I also want some current print specials I am running included.
-double your order FREE (order 500 business cards and get 1000)
-250 100lb gloss stock brochures 99.00
-business packages (cards, envelopes and letterhead) 299
-1000 flyers 140.40
-5000 postcards 179.99
A list of services
banners
booklets
brochures
business cards
calendars
catalogs
CD/DVD packages
envelopes
event tickets
flyers
hangtags
postcards
posters
presentation folders
rack cards
labels
table tents
window cling and decal
"order 24/7 orders@quillory.example" must be included
my logo is Quillory will be supplied later
ive received some great designs. however Im looking for something a little more modern like some tavren would put out. if the amount of words is too much please feel free to edit. also an idea i had for the list of services i offer is to have it transparent yet readable as the background of the postcard some small some big but covering the entire backgroud. you can then design on top of that with other thing. just an early morning thought
Reason: I have uploaded a sketch of my idea, please take time to look at it for an accurate depiction of what im looking for. feel free to add elements that make it pop off the page
Reason: We are getting close i will be providing feed back today

```html
<!DOCTYPE html>
<html lang="en">
<head>
<meta charset="utf-8">
<title>Quillory – Direct Mail Postcard</title>
<link rel="stylesheet" href="https://fonts.googleapis.com/css2?family=Montserrat:wght@600;700&family=Open+Sans:ital,wght@0,400;1,700&family=Roboto+Slab:wght@200;300;400;600&display=swap">
<style>
  :root{
    --ink-black:#000;
    --paper:#fff;
    --foil-gold:#c9a25a;
    --foil-gold-soft:#e9c98a;
    --auto-blue:#2b7bc0;
    --dental-blue:#1f86d0;
    --estate-green:#8cc63f;
    --text-grey:#222;
    --muted-grey:#6a6a6a;
    --cloud-grey:#8a8a8a;
    --rule-grey:#9a9a9a;
  }
  *{box-sizing:border-box;margin:0;padding:0}
  html,body{width:1200px;height:420px;overflow:hidden;background:var(--paper)}
  body{position:relative;font-family:"Roboto Slab",serif}

  .postcard{position:absolute;top:18px;height:390px;overflow:hidden;box-shadow:3px 4px 6px rgba(0,0,0,.35)}

  /* front */
  .postcard--front{left:46px;width:562px;background:var(--ink-black);color:var(--paper)}
  .front__ornament{position:absolute;right:0;top:0;width:170px;height:140px;
    background:radial-gradient(circle at 65% 30%,rgba(201,162,90,.55),rgba(201,162,90,.2) 45%,transparent 72%)}
  .front__headline{position:absolute;left:22px;top:16px;font-family:"Roboto Slab",serif;font-weight:200;
    font-size:38px;line-height:44px;letter-spacing:1px;text-transform:uppercase}
  .front__order{position:absolute;left:22px;top:118px;font-family:"Montserrat",sans-serif;font-weight:600;font-size:16.5px}

  .sample{position:absolute;overflow:hidden}
  .sample--dental{left:0;top:246px;width:175px;height:150px;background:linear-gradient(110deg,#6b4318,#a0712f 55%,#3a2208)}
  .sample--dental .sample__photo{position:absolute;inset:0 0 50px 0}
  .dental__title{position:absolute;left:10px;top:25px;font-family:"Open Sans",sans-serif;font-size:27px;color:#fff}
  .dental__tag{position:absolute;left:10px;top:57px;font-family:"Open Sans",sans-serif;font-style:italic;font-size:15px;color:#fff}
  .dental__band{position:absolute;left:0;bottom:0;width:100%;height:52px;background:var(--dental-blue);color:#fff;font-family:"Open Sans",sans-serif}
  .dental__brand{position:absolute;left:10px;top:6px;font-weight:700;font-size:17px;font-style:normal}
  .dental__brand span{display:block;font-weight:400;font-size:13px;line-height:14px}
  .dental__note{position:absolute;left:82px;top:10px;width:90px;font-size:8px;font-style:italic;line-height:11px}

  .sample--estate{left:352px;top:168px;width:230px;height:140px;background:var(--estate-green);transform:rotate(-14deg);color:#fff;font-family:"Open Sans",sans-serif}
  .estate__title{position:absolute;left:18px;top:22px;font-size:11px;line-height:14px;width:80px}
  .estate__art{position:absolute;left:120px;top:18px;width:80px;height:62px;background:linear-gradient(135deg,rgba(255,255,255,.35),rgba(255,255,255,.1))}
  .estate__contact{position:absolute;left:18px;top:88px;font-size:7px;line-height:11px}

  .sample--auto{left:128px;top:178px;width:305px;height:215px;background:#fff;transform:rotate(10deg);color:var(--text-grey);font-family:"Open Sans",sans-serif}
  .auto__title{position:absolute;left:14px;top:10px;color:var(--auto-blue);font-weight:700;font-style:normal;font-size:36px;line-height:36px}
  .auto__title span{display:block;color:#5c5c5c;font-size:19px;line-height:22px}
  .auto__photo{position:absolute;left:120px;top:55px;width:185px;height:160px;background:linear-gradient(160deg,#8a8a7e,#d9d9d4 45%,#f4f4f4 70%,#bdbdbd)}
  .auto__copy{position:absolute;left:14px;top:100px;width:110px;font-size:9.5px;line-height:12px;color:#8a8a8a}
  .auto__small{position:absolute;left:14px;top:193px;font-size:5px;color:#999}

  .front__logo{position:absolute;right:34px;top:342px;text-align:right;font-family:"Open Sans",sans-serif;font-weight:700;font-size:17px;line-height:18px;color:#fff}
  .front__logo span{display:block}

  /* back */
  .postcard--back{left:623px;width:539px;background:var(--paper);color:var(--text-grey)}
  .back__ornament{position:absolute;right:0;top:0;width:200px;height:180px;
    background:radial-gradient(circle at 70% 22%,rgba(233,201,138,.75),rgba(233,201,138,.3) 40%,transparent 70%)}
  .back__stamp{position:absolute;left:445px;top:28px;width:66px;height:72px;border:1px solid #555}
  .services{position:absolute;left:17px;top:14px;font-family:"Open Sans",sans-serif;font-style:italic;font-weight:700;
    font-size:26px;line-height:21.5px;letter-spacing:-.5px;color:var(--cloud-grey);white-space:nowrap;list-style:none}
  .services li{display:inline}
  .services .row{display:block}
  .services .tone-2{opacity:.55}
  .services .tone-3{opacity:.32}
  .services .tone-4{opacity:.18}
  .services__fade{position:absolute;left:190px;top:0;width:260px;height:170px;background:linear-gradient(90deg,rgba(255,255,255,0),#fff 85%)}

  .back__pitch{position:absolute;left:19px;top:192px;width:245px;font-weight:300;font-size:11px;line-height:14px;color:var(--text-grey)}
  .specials{position:absolute;left:19px;top:259px;list-style:none;font-weight:300;font-size:11px;line-height:14px}
  .specials li::before{content:"» "}
  .back__visit{position:absolute;left:19px;top:353px;font-weight:300;font-size:10px}
  .back__visit strong{font-weight:600}
  .address-lines{position:absolute;left:277px;top:184px;width:235px}
  .address-lines span{display:block;border-top:1px solid var(--rule-grey);height:32.5px}
  .back__logo{position:absolute;right:30px;top:330px;text-align:right;font-family:"Open Sans",sans-serif;font-weight:700;font-size:13px;line-height:14px;color:#b0b0b0}
  .back__logo span{display:block}
</style>
</head>
<body>

<section class="postcard postcard--front">
  <div class="front__ornament" role="img" aria-label="Gold foil ornamental medallion"></div>
  <h1 class="front__headline">Let us make your<br>bussiness shine !</h1>
  <p class="front__order">order 24/7 orders@quillory.example</p>

  <article class="sample sample--dental">
    <div class="sample__photo" role="img" aria-label="Warm-toned dental practice photo"></div>
    <p class="dental__title">Smile</p>
    <p class="dental__tag">with confidence</p>
    <div class="dental__band">
      <p class="dental__brand">ABC<span>dentists</span></p>
      <p class="dental__note">Gentle care for every smile, all year.</p>
    </div>
  </article>

  <article class="sample sample--estate">
    <p class="estate__title">We are<br>real estate</p>
    <div class="estate__art" role="img" aria-label="Hand-drawn house sketch"></div>
    <p class="estate__contact">12 Main Street, City<br>call us today</p>
  </article>

  <article class="sample sample--auto">
    <div class="auto__photo" role="img" aria-label="Photo of a white car in motion with foil headlights"></div>
    <p class="auto__title">Auto<span>company</span></p>
    <p class="auto__copy">Lorem ipsum dolor sit amet, consetetur sadip scing elitr, sed diam nonumy eirmod</p>
    <p class="auto__small">Lorem ipsum dolor sit amet, consetetur sed.</p>
  </article>

  <p class="front__logo">Quillory<span>logo</span></p>
</section>

<section class="postcard postcard--back">
  <div class="back__ornament" role="img" aria-label="Gold foil ornamental medallion"></div>
  <ul class="services">
    <li class="row">business cards<span class="tone-2">brochures</span><span class="tone-3">banners</span></li>
    <li class="row tone-3">calendarscatalogsCD/DVD packages</li>
    <li class="row">envelopes<span class="tone-4">event ticketsflyers</span></li>
    <li class="row">postcards<span class="tone-3">posterspresentation folders</span></li>
    <li class="row tone-2">window cling and decal</li>
    <li class="row tone-4">rack cardslabels</li>
    <li class="row tone-4">table tents</li>
  </ul>
  <div class="services__fade"></div>
  <div class="back__stamp"></div>

  <p class="back__pitch">business with no limits, meet mailing with no addresses, gain new customers through "Open Lane Parcel Drop" reach new customers at their home without needing their address.</p>
  <ul class="specials">
    <li>double your order FREE</li>
    <li>250 100lb gloss stock brochures 99.00</li>
    <li>business packages 299</li>
    <li>1000 flyers 140.40</li>
    <li>5000 postcards 179.99</li>
  </ul>
  <p class="back__visit">visit <strong>yourwebsite.com</strong> for more info.</p>

  <div class="address-lines"><span></span><span></span><span></span><span></span></div>
  <p class="back__logo">Quillory<span>logo</span></p>
</section>

</body>
</html>
```